Business Card Design

We would like a colorful, engaging, welcoming business card, utilizing our picture of a local lighthouse. We are a Church. We would like the design to mostly feature the colour blue.
Updates
Project Deadline Extended
Reason: Because of some suggested changes that have been sent out
Thank you so much to all Designers who sent in submissions to us - it was really hard to make a decision, they were all of such high quality. We would not hesitate to recommend Sketch Harbor to other churches/ businesses.
Kestrel Beacon Fellowship
Industry/Entity Type
Business
Contact Information for Business Card
Kestrel Beacon Fellowship Inc, 17 Marrick Rd, TOVERDALE WA 6391, Ph: (08) 9517 4063, E: beaconfellowship@quorvamail.example, Facebook logo - Kestrel Beacon Fellowship Inc, Sunday Service 10am, "For God sent not his Son into the world to condemn the world; but that the world through Him might be saved." John 3:17.
Look and feel
Each slider illustrates characteristics of the customer's brand and the style your logo design should communicate.

```html
<!DOCTYPE html>
<html lang="en">
<head>
<meta charset="utf-8">
<title>Kestrel Beacon Fellowship – Business Card</title>
<link rel="stylesheet" href="https://fonts.googleapis.com/css2?family=Libre+Baskerville:wght@400;700&family=Crimson+Pro:wght@400&display=swap">
<style>
  :root {
    --ink-blue: #2553b0;
    --paper: #ffffff;
    --sky-deep: #0a2466;
    --sky-mid: #1d55b8;
    --heath-dark: #26332c;
    --heath-sage: #6c8c8c;
    --heath-low: #3d4a3c;
  }
  html, body {
    margin: 0;
    padding: 0;
    width: 1200px;
    height: 741px;
    overflow: hidden;
    background: var(--paper);
  }
  .card {
    position: relative;
    width: 1200px;
    height: 741px;
    background: var(--paper);
  }
  .card__photo {
    position: absolute;
    inset: 0;
  }
  .card__verse {
    position: absolute;
    left: 77px;
    top: 92px;
    margin: 0;
    width: 470px;
    font-family: "Libre Baskerville", "Baskerville", serif;
    font-weight: 700;
    font-size: 33px;
    line-height: 54px;
    color: var(--ink-blue);
    letter-spacing: -0.4px;
  }
  .card__contact {
    position: absolute;
    left: 77px;
    top: 598px;
    display: flex;
    font-family: "Crimson Pro", "Georgia", serif;
    font-style: normal;
    font-size: 24.5px;
    line-height: 39px;
    color: var(--ink-blue);
  }
  .contact__org {
    padding-right: 12px;
  }
  .contact__reach {
    padding-left: 12px;
    border-left: 2px solid var(--ink-blue);
  }
  .contact__line {
    display: block;
    white-space: nowrap;
  }
</style>
</head>
<body>
  <div class="card">
    <svg class="card__photo" width="1200" height="741" viewBox="0 0 1200 741" role="img" aria-label="Photo of a lit lighthouse on a heath-covered headland under a blue night sky with light beams">
      <defs>
        <linearGradient id="photoTone" x1="0" y1="0" x2="0" y2="1">
          <stop offset="0" stop-color="var(--sky-deep)"/>
          <stop offset="0.28" stop-color="var(--sky-mid)"/>
          <stop offset="0.45" stop-color="var(--heath-dark)"/>
          <stop offset="0.75" stop-color="var(--heath-sage)"/>
          <stop offset="1" stop-color="var(--heath-low)"/>
        </linearGradient>
      </defs>
      <path fill="url(#photoTone)" d="M877 0 H1200 V741 H877 V356 Q877 346 867 346 H625 Q613 346 613 334 V100 Q613 88 625 88 H867 Q877 88 877 78 Z"/>
    </svg>

    <p class="card__verse">„For God sent not his Son into the world to condemn the world; but that the world through Him might be saved.“ John 3/17</p>

    <address class="card__contact">
      <div class="contact__org">
        <span class="contact__line">Kestrel Beacon Fellowship Inc</span>
        <span class="contact__line">17 Marrick Rd, Toverdale WA 6391</span>
      </div>
      <div class="contact__reach">
        <span class="contact__line">beaconfellowship@quorvamail.example</span>
        <span class="contact__line">(08) 9517 4063</span>
      </div>
    </address>
  </div>
</body>
</html>
```